Creative & Professional Business Card for hair salon

We are looking to update our business cards. Our salon is creative, modern, progressive and professional and looking for a design that will reflect this.

```html
<!DOCTYPE html>
<html lang="en">
<head>
<meta charset="utf-8">
<title>Sky Loft Studio – Business Cards</title>
<link rel="stylesheet" href="https://fonts.googleapis.com/css2?family=Questrial&display=swap">
<style>
  :root {
    --bg: #1e1e1f;
    --card-dark: #393a3c;
    --text-light: #e4e5e7;
    --text-muted: #c3c5c8;
    --brand-ink: #2f3135;
    --sky-deep: #3f8ad6;
    --sky-soft: #8fc0ec;
    --rule-line: #c9cbce;
  }
  * { box-sizing: border-box; margin: 0; padding: 0; }
  html, body { width: 1200px; height: 997px; overflow: hidden; }
  body {
    background: var(--bg);
    font-family: "Questrial", "Century Gothic", sans-serif;
    display: flex;
    flex-direction: column;
    align-items: center;
    justify-content: center;
    gap: 70px;
  }
  .card {
    width: 760px;
    height: 380px;
    background: var(--card-dark);
    position: relative;
    overflow: hidden;
    box-shadow: 0 18px 40px rgba(0,0,0,.5);
  }
  .sky {
    position: absolute;
    left: 0; top: 0;
    width: 100%;
    height: 215px;
    background: linear-gradient(180deg, var(--sky-soft) 0%, var(--sky-deep) 100%);
  }
  .brand {
    position: absolute;
    left: 0; right: 0;
    top: 78px;
    display: flex;
    align-items: center;
    justify-content: center;
    gap: 14px;
    color: var(--brand-ink);
    font-size: 34px;
    line-height: 1.2;
    letter-spacing: 1px;
  }
  .brand-dot {
    width: 14px; height: 14px;
    border-radius: 50%;
    background: var(--brand-ink);
  }
  .panel {
    position: absolute;
    left: 0; right: 0;
    top: 215px;
    bottom: 0;
    text-align: center;
    color: var(--text-light);
  }
  .cta {
    margin-top: 18px;
    font-size: 20px;
    line-height: 1.2;
    letter-spacing: 1.5px;
    text-transform: uppercase;
  }
  .rule { display: block; margin: 8px auto 10px; }
  .contact {
    list-style: none;
    font-family: "Questrial", "Century Gothic", sans-serif;
    font-size: 16px;
    line-height: 1.4;
    color: var(--text-muted);
  }
  .next-label {
    margin-top: 26px;
    font-size: 16px;
    letter-spacing: 2px;
    text-transform: uppercase;
    color: var(--text-muted);
  }
  .write-lines { display: block; margin: 20px auto 0; }
</style>
</head>
<body>

  <section class="card card-back">
    <div class="sky" role="img" aria-label="Photo of a bright blue sky with white clouds and sun rays"></div>
    <div class="brand"><span class="brand-dot"></span><span>Sky Loft Studio by Lena Marsh</span></div>
    <div class="panel">
      <p class="next-label">Next Appointment</p>
      <svg class="write-lines" width="560" height="70" viewBox="0 0 560 70">
        <line x1="0" y1="15" x2="560" y2="15" stroke="var(--rule-line)" stroke-width="1.5" stroke-dasharray="2 4"/>
        <line x1="0" y1="60" x2="560" y2="60" stroke="var(--rule-line)" stroke-width="1.5" stroke-dasharray="2 4"/>
      </svg>
    </div>
  </section>

  <section class="card card-front">
    <div class="sky" role="img" aria-label="Photo of a bright blue sky with white clouds and sun rays"></div>
    <div class="brand"><span class="brand-dot"></span><span>Sky Loft Studio by Lena Marsh</span></div>
    <div class="panel">
      <p class="cta">Call us or book an appointment online</p>
      <svg class="rule" width="160" height="4" viewBox="0 0 160 4">
        <defs>
          <linearGradient id="rule-fade" x1="0" x2="1">
            <stop offset="0" stop-color="#ffffff" stop-opacity="0"/>
            <stop offset=".5" stop-color="#ffffff" stop-opacity=".9"/>
            <stop offset="1" stop-color="#ffffff" stop-opacity="0"/>
          </linearGradient>
        </defs>
        <rect width="160" height="3" fill="url(#rule-fade)"/>
      </svg>
      <ul class="contact">
        <li>07 5500 1234</li>
        <li>salon@skyloftstudio.com.au</li>
        <li>skyloftstudiobylenamarsh</li>
        <li>5/12 Harbour Lane, Coastview Qld 4000</li>
      </ul>
    </div>
  </section>

</body>
</html>
```